Flowy subpage design wanted for a modern tax/accounting firm in Switzerland

--- Introduction ---
We are a tax and accounting firm in Switzerland. We provide services for expats living in Switzerland, our service is quite exclusive and modern (digital).

We just relaunched our website www.fiscaverde.ch and are happy with the design, so the desired subpage (more details below) should of course fit in.

--- Main brief ---
Please see Word File attached. The page has to include the whole text (11 chapters). A very intuitive, flowy design on only one subpage (not one page per chapter) is a MUST. Also, it is key that the design is supporting the content of the individual chapters, so it would be advantageous if you'd have a good unterstanding of the text attached.

--- Further information ---
A similar example would be this one: https://www2.brennmark.com/ch/en/pages/tax/articles/living-working-switzerland.html

This one is similar in what concerns the content, but NOT what we are looking for designwise. It is very simple and looks "thrown together", just not aesthetically pleasing in our opinion.

--- Final thoughts ---
- If you blow our minds with your design, we will certainly have future work for you.
- Our clients are between 20-50 years old, well educated, high income / high wealth, English speaking and living in Switzerland.
- CI/CD information:
Fonts
Montserrat regular / medium italic / bold
Colors
White #ffffffff
Darkblue #0a2b46
Darkblue 25% #b5bfc8
Darkblue 50% #8595a4
Greenblue #0d4261

We are looking forward to your designs!
Updates

Thank you very much for the submitted designs and your efforts. Unfortunately, none of the designs meet our expectations so far. Please note the following: - Designs that do not take CI into account will not be looked at more closely. - We have received many simple designs with very simple structure and accordion elements. But more important than the simple structure is an eye-catching design! Make it flowy and beautiful - We don't want pictures of Swiss vehicles, passes or other pictures that don't actively support the text. If you can make an illustration that really fits the context, fine, otherwise better leave it without. Thank you

Target Market(s)

Expats living in Switzerland. High income earners / high net worth individuals

Industry/Entity Type

tax/accounting

Number of Pages Required

1 page

Font styles to use
Other font styles liked:
• Montserrat

Colors
0054AA
0677BA
7BADD7
CADEEF
E8F1F8

Requirements
Must have
• based on general website design
Nice to have
• intuitive, flowy, attractive representation of much text
Should not have
• basic copy/paste of the text in sections :)

```html
<!DOCTYPE html>
<html lang="en">
<head>
<meta charset="utf-8">
<title>Living and Working in CH – Expat Tax Guide</title>
<link rel="stylesheet" href="https://fonts.googleapis.com/css2?family=Montserrat:ital,wght@0,300;0,400;0,500;0,600;0,700;1,500&display=swap">
<style>
:root{
  --stage:#1c2935;
  --white:#ffffff;
  --darkblue:#0a2b46;
  --greenblue:#0d4261;
  --db25:#b5bfc8;
  --db50:#8595a4;
  --blue:#0054aa;
  --blue-mid:#0677ba;
  --blue-light:#7badd7;
  --blue-pale:#cadeef;
  --blue-mist:#e8f1f8;
  --text:#3a4b5c;
  --line:#e3e8ee;
}
*{box-sizing:border-box;margin:0;padding:0}
html,body{width:1200px;height:3124px;overflow:hidden}
body{background:var(--stage);font-family:"Montserrat",sans-serif;color:var(--text);position:relative}
.page{position:absolute;left:72px;top:0;width:1056px;height:3124px;background:var(--white);overflow:hidden}

/* header */
.site-header{position:absolute;left:0;top:0;width:100%;height:112px;display:flex;align-items:center;justify-content:space-between;padding:0 56px 0 48px}
.brand{display:flex;align-items:center;gap:12px;font-weight:700;font-size:17px;letter-spacing:2px;color:var(--darkblue);text-transform:uppercase}
.brand-dot{width:30px;height:30px;border-radius:50%;background:var(--darkblue)}
.main-nav{display:flex;gap:30px;font-size:12px;color:var(--darkblue)}
.main-nav a{color:inherit;text-decoration:none;padding:6px 0}
.main-nav .is-active{border-bottom:2px solid var(--darkblue);font-weight:600}

/* hero */
.hero{position:absolute;left:0;top:112px;width:100%;height:200px;background:linear-gradient(100deg,var(--greenblue),var(--darkblue))}
.hero svg{position:absolute;inset:0}
.hero h1{position:absolute;left:0;right:0;top:62px;text-align:center;color:var(--white);font-weight:300;font-size:40px;letter-spacing:1px}
.hero h1 b{font-weight:700}

/* section shared */
.chapter{position:absolute;left:0;width:100%}
.chapter-num{position:absolute;left:24px;width:62px;height:62px;background:#eef1f4;color:var(--db50);font-size:24px;font-weight:500;display:flex;align-items:center;justify-content:center}
.chapter-title{position:absolute;left:128px;width:520px;font-size:40px;line-height:1.15;font-weight:700;color:var(--darkblue)}
.chapter-intro{position:absolute;left:128px;width:520px;font-size:11px;line-height:1.7;color:var(--db50)}
.card{position:absolute;left:212px;width:790px;background:var(--white);box-shadow:0 12px 40px rgba(10,43,70,.14);display:flex}
.card-nav{width:190px;padding:28px 0 28px 0;border-right:1px solid var(--line)}
.card-nav li{list-style:none;font-size:9.5px;line-height:1.4;padding:9px 20px;color:var(--db50);border-bottom:1px solid var(--line)}
.card-nav li.is-current{color:var(--darkblue);font-weight:600;border-left:3px solid var(--darkblue)}
.card-body{flex:1;padding:30px 40px 34px 40px}
.card-body h3{font-size:20px;font-weight:600;color:var(--darkblue);margin-bottom:14px}
.card-body p{font-size:10.5px;line-height:1.75;margin-bottom:12px;color:var(--text)}
.card-body .lead-in{font-weight:700;color:var(--darkblue)}
.more-btn{display:inline-block;margin-top:10px;padding:10px 26px;border:1px solid var(--db25);font-size:10px;font-weight:600;color:var(--darkblue);letter-spacing:.5px}

/* chapter 01 */
.ch1{top:312px;height:760px}
.ch1 .chapter-num{top:64px}
.ch1 .chapter-title{top:56px}
.ch1 .chapter-intro{top:160px}
.ch1 .card{top:248px;height:470px}
.lang-tags{display:flex;gap:12px;margin:4px 0 18px}
.lang-tag{flex:1;padding:9px 0;text-align:center;font-size:10px;font-weight:600}
.lang-tag.de{background:#fde6e6;color:#b0505a}
.lang-tag.fr{background:var(--blue-mist);color:var(--blue)}
.lang-tag.it{background:#e3f3ea;color:#3f8a5f}
.lang-tag.rm{background:#fbf1dc;color:#a07a2c}
.card-body h3.second{margin-top:18px}

/* chapter 02 */
.ch2{top:1040px;height:680px}
.ch2-bg{position:absolute;inset:0}
.ch2 .chapter-num{top:112px;background:var(--greenblue);color:var(--db25)}
.ch2 .chapter-title{top:104px;color:var(--white);width:600px;font-size:38px}
.ch2 .chapter-intro{top:250px;color:var(--db25);width:560px}
.ch2 .card{top:320px;height:250px;background:var(--greenblue);box-shadow:0 12px 40px rgba(0,0,0,.25)}
.ch2 .card-nav{border-right-color:rgba(255,255,255,.12)}
.ch2 .card-nav li{color:var(--db50);border-bottom-color:rgba(255,255,255,.1)}
.ch2 .card-nav li.is-current{color:var(--white);border-left-color:var(--white)}
.ch2 .card-body h3{color:var(--white);font-size:19px;line-height:1.4;font-weight:600;width:420px}
.ch2 .card-body p{color:var(--db25)}
.ch2 .more-btn{color:var(--white);border-color:var(--db50)}

/* chapter 03 */
.ch3{top:1720px;height:1404px}
.ch3 .chapter-num{top:40px}
.ch3 .chapter-title{top:32px;width:600px}
.ch3 .chapter-intro{top:136px;width:560px}
.ch3 .card{top:222px;height:1050px}
.ch3 .card-body h3{margin-top:8px}
.permit-block{margin-bottom:22px}
.state-grid{display:grid;grid-template-columns:repeat(4,1fr);gap:8px;margin:6px 0 16px}
.state-grid span{border:1px solid var(--line);background:#f6f8fa;padding:9px 0;text-align:center;font-size:9.5px;color:var(--darkblue)}

.to-top{position:absolute;left:0;right:0;top:1340px;display:flex;flex-direction:column;align-items:center;gap:8px;font-size:9px;color:var(--db50);letter-spacing:1px}
.to-top svg{display:block}
</style>
</head>
<body>
<div class="page">

  <header class="site-header">
    <div class="brand"><span class="brand-dot"></span>Fiscaverde Advisory</div>
    <nav class="main-nav">
      <a href="#">Home</a>
      <a href="#">Tax-Journey</a>
      <a href="#">What's up today?</a>
      <a href="#" class="is-active">Expat tax guide</a>
      <a href="#">About us</a>
    </nav>
  </header>

  <section class="hero">
    <svg width="1056" height="200" viewBox="0 0 1056 200" aria-hidden="true">
      <polygon points="0,120 1056,40 1056,200 0,200" fill="#ffffff" opacity=".04"/>
      <polygon points="300,200 1056,90 1056,200" fill="#ffffff" opacity=".05"/>
    </svg>
    <h1>Living Work <b>in CH</b></h1>
  </section>

  <!-- Chapter 01 -->
  <section class="chapter ch1">
    <div class="chapter-num">01</div>
    <h2 class="chapter-title">Life in<br>Swihzerland</h2>
    <p class="chapter-intro">Switzerland is known for its high quality of life, stable economy and stunning landscapes. Here is what expats should know about the languages, the currency and everyday banking before moving.</p>
    <div class="card">
      <ul class="card-nav">
        <li class="is-current">Overview</li>
        <li>Languages and regional differences</li>
        <li>Currency and banking</li>
        <li>Cost of living</li>
        <li>Health insurance</li>
        <li>Public transport network</li>
      </ul>
      <div class="card-body">
        <h3>4 official languages</h3>
        <div class="lang-tags">
          <span class="lang-tag de">German</span>
          <span class="lang-tag fr">French</span>
          <span class="lang-tag it">Italian</span>
          <span class="lang-tag rm">Romansh</span>
        </div>
        <p>Swiss German is spoken by about two thirds of the population, mainly in the north, centre and east. French dominates the west, Italian is spoken in Ticino and parts of Graubünden.</p>
        <p>Romansh is spoken by a small minority in Graubünden. English is widely understood in business, especially in the larger cities and international companies.</p>
        <p><span class="lead-in">Good to know:</span> learning the local language helps a lot with everyday life, integration and the application for a settlement permit.</p>
        <h3 class="second">Currency and banking</h3>
        <p>The Swiss currency is the <span class="lead-in">Swiss franc (CHF)</span>. One franc is divided into 100 centimes. Coins and notes are used alongside cards and mobile payments.</p>
        <p>To open a bank account you usually need a passport, a residence permit and proof of address. Account fees vary, so comparing offers is worth it.</p>
        <span class="more-btn">Read more</span>
      </div>
    </div>
  </section>

  <!-- Chapter 02 -->
  <section class="chapter ch2">
    <svg class="ch2-bg" width="1056" height="680" viewBox="0 0 1056 680" aria-hidden="true">
      <defs>
        <linearGradient id="ch2Fill" x1="0" y1="0" x2="1" y2="1">
          <stop offset="0" stop-color="#0d4261"/>
          <stop offset="1" stop-color="#0a2b46"/>
        </linearGradient>
      </defs>
      <polygon points="0,30 528,0 1056,40 1056,640 528,680 0,630" fill="url(#ch2Fill)"/>
      <polygon points="0,30 528,0 1056,40 1056,120 0,200" fill="#ffffff" opacity=".04"/>
    </svg>
    <div class="chapter-num">02</div>
    <h2 class="chapter-title">Switzerland - a brief overview of the Alpine country</h2>
    <p class="chapter-intro">A small country in the heart of Europe with a federal structure, direct democracy and a strong economy. Here are the key facts about its political system and regions.</p>
    <div class="card">
      <ul class="card-nav">
        <li class="is-current">Political system</li>
        <li>Cantons and communes</li>
        <li>Direct democracy</li>
        <li>Economy and labour</li>
      </ul>
      <div class="card-body">
        <h3>Switzerland is divided into 26 cantons, which have partial sovereignty and a capital.</h3>
        <p>Each canton has its own constitution, parliament and tax laws. This is why tax rates can differ widely between cantons and even between communes within the same canton.</p>
        <span class="more-btn">Read more</span>
      </div>
    </div>
  </section>

  <!-- Chapter 03 -->
  <section class="chapter ch3">
    <div class="chapter-num">03</div>
    <h2 class="chapter-title">Immigrating to Switzerland - These options are available</h2>
    <p class="chapter-intro">Anyone who wants to live and work in Switzerland needs a permit. Which one you receive depends on your nationality, your employment contract and the planned length of your stay.</p>
    <div class="card">
      <ul class="card-nav">
        <li>Overview of permits</li>
        <li class="is-current">Residence and work permits in Switzerland</li>
        <li>Family reunification</li>
        <li>Registration process</li>
      </ul>
      <div class="card-body">
        <div class="permit-block">
          <h3>Short term residence permit (L permit)</h3>
          <p>The L permit is issued for stays of up to one year and is tied to a specific employment contract. For citizens of EU/EFTA states it can be renewed if the contract is extended.</p>
          <p>Nationals of other countries receive it only in limited numbers and when qualified staff cannot be found on the local market. A change of job usually requires a new approval.</p>
        </div>
        <div class="permit-block">
          <h3>Residence permit (B permit)</h3>
          <p>The B permit is granted to foreign nationals who live in Switzerland for a longer period with a certain purpose, such as employment of at least twelve months.</p>
          <p>For EU/EFTA citizens it is valid for five years. For third country nationals it is usually valid for one year and renewed annually. Holders of a B permit pay tax at source on their salary.</p>
        </div>
        <div class="permit-block">
          <h3>Settlement permit (C permit)</h3>
          <p>The C permit grants the right to unlimited residence. Citizens of the following states may apply after five years of regular residence:</p>
          <div class="state-grid">
            <span>Belgium</span><span>Denmark</span><span>Germany</span><span>France</span>
            <span>Greece</span><span>Italy</span><span>Liechtenstein</span><span>Luxembourg</span>
            <span>Netherlands</span><span>Austria</span><span>Portugal</span><span>Spain</span>
            <span>Iceland</span><span>Norway</span><span>Finland</span><span>Sweden</span>
          </div>
          <p>Citizens of other countries can usually apply after ten years. Good language skills and successful integration may allow an earlier application.</p>
        </div>
        <div class="permit-block">
          <h3>Cross-border commuter permit (G permit)</h3>
          <p>The G permit is for people who live in a neighbouring country and work in Switzerland. Holders must return to their place of residence at least once a week.</p>
          <p>For EU/EFTA citizens the permit is valid for five years with an open-ended contract. Taxation depends on the agreement between Switzerland and the country of residence.</p>
        </div>
        <span class="more-btn">Read more</span>
      </div>
    </div>
    <div class="to-top">
      <svg width="26" height="26" viewBox="0 0 26 26" aria-hidden="true">
        <circle cx="13" cy="13" r="12" fill="none" stroke="#b5bfc8"/>
        <path d="M8 15l5-5 5 5" fill="none" stroke="#8595a4" stroke-width="1.5"/>
      </svg>
      BACK TO TOP
    </div>
  </section>

</div>
</body>
</html>
```